Eye Catching Business Card for Optometrist

We've recently refreshed our logo and now we need a fresh and bold look for our business cards. We provide progressive ways to improve people's vision and protect their eye health.

Use our new logo as guidance into the colors to use. As far as style goes, I love how bold and eye catching the card is for Lanternfly Studio. Feel free to use your creative judgement.

Tagline: "Sharper Sight For Every Day."

pertinent info to include:

Dr. Martin Sowerby
Optometrist

2857 Bramwell Ridge Blvd #217
Harlow Springs, MO 63411
(555) 382-7190

marty@brightlenshomeoptics.example
www.brightlenshomeoptics.example

```html
<!DOCTYPE html>
<html lang="en">
<head>
<meta charset="utf-8">
<title>Bright Lens Home Optics – Business Card</title>
<link rel="stylesheet" href="https://fonts.googleapis.com/css2?family=PT+Sans+Narrow:wght@400;700&family=Open+Sans:wght@400;700&display=swap">
<style>
  :root {
    --backdrop: #d9d9d9;
    --card: #ffffff;
    --red: #d4202f;
    --brown: #5a4535;
    --tan: #d9c1a0;
    --ink: #5a4a40;
  }
  * { margin: 0; padding: 0; box-sizing: border-box; }
  html, body {
    width: 1200px;
    height: 787px;
    overflow: hidden;
    background: var(--backdrop);
  }
  .card {
    position: absolute;
    left: 100px;
    top: 108px;
    width: 1000px;
    height: 571px;
    background: var(--card);
    font-family: "PT Sans Narrow", sans-serif;
    overflow: hidden;
  }

  .edge-strip {
    position: absolute;
    left: 0;
    top: 0;
    width: 28px;
    height: 100%;
    display: flex;
    flex-direction: column;
  }
  .edge-strip span { display: block; }

  .footer-band {
    position: absolute;
    left: 0;
    bottom: 0;
    width: 100%;
    height: 44px;
    display: flex;
  }
  .footer-band span { display: block; height: 100%; }

  .seg--red { background: var(--red); }
  .seg--tan { background: var(--tan); }
  .seg--brown { background: var(--brown); }

  .brand {
    position: absolute;
    left: 64px;
    top: 44px;
    display: flex;
    align-items: center;
    gap: 16px;
  }
  .brand__mark {
    width: 48px;
    height: 48px;
    border-radius: 50%;
    background: var(--red);
  }
  .brand__name {
    font-family: "Open Sans", sans-serif;
    font-weight: 700;
    font-size: 28px;
    color: var(--red);
    text-transform: uppercase;
    letter-spacing: 0.5px;
  }
  .tagline {
    position: absolute;
    left: 64px;
    top: 118px;
    font-family: "Open Sans", sans-serif;
    font-size: 22px;
    color: var(--ink);
  }
  .tagline strong { color: var(--red); font-weight: 700; }

  .doctor {
    position: absolute;
    right: 48px;
    top: 40px;
    text-align: right;
    line-height: 1.15;
  }
  .doctor__name { font-size: 36px; color: var(--red); }
  .doctor__title { font-size: 32px; color: var(--ink); }

  .contact {
    position: absolute;
    left: 64px;
    top: 215px;
    width: 872px;
    text-align: center;
    line-height: 1.2;
  }
  .contact__street, .contact__city { font-size: 36px; color: var(--red); }
  .contact__street .num { color: var(--ink); }
  .contact__phone { font-size: 30px; color: var(--red); margin-top: 14px; }
  .contact__email { font-size: 28px; font-weight: 700; color: var(--ink); margin-top: 10px; }
  .contact__web { font-size: 30px; font-weight: 700; color: var(--red); margin-top: 4px; }
</style>
</head>
<body>
  <main class="card">
    <div class="edge-strip">
      <span class="seg--red" style="height:45%;"></span>
      <span class="seg--tan" style="height:30%;"></span>
      <span class="seg--brown" style="height:25%;"></span>
    </div>

    <div class="brand">
      <span class="brand__mark"></span>
      <span class="brand__name">Bright Lens Home Optics</span>
    </div>
    <p class="tagline"><strong>Sharper Sight</strong> For Every Day</p>

    <div class="doctor">
      <p class="doctor__name">Dr. Martin Sowerby</p>
      <p class="doctor__title">Optometrist</p>
    </div>

    <div class="contact">
      <p class="contact__street"><span class="num">2857</span> Bramwell Ridge Blvd #217</p>
      <p class="contact__city">Harlow Springs, MO 63411</p>
      <p class="contact__phone">(555) 382-7190</p>
      <p class="contact__email">marty@brightlenshomeoptics.example</p>
      <p class="contact__web">www.brightlenshomeoptics.example</p>
    </div>

    <div class="footer-band">
      <span class="seg--brown" style="width:28px;"></span>
      <span class="seg--tan" style="width:62%;"></span>
      <span class="seg--red" style="width:20%;"></span>
      <span class="seg--brown" style="flex:1;"></span>
    </div>
  </main>
</body>
</html>
```